redesing professional certificate

Redesign our certificate to more a professional look and to make it look like a-wanna have - Best in adobe photoshop, because this template will be our basic, and we have in our education different levels, basic, upper, lower, complex, master level. I usually add a small picture to show what level they are. Or when you have a better suggestion I a gladly to hear.
We teach to physiotherapist so it has to look professional.

Target Market(s)

physiotherapist

Industry/Entity Type

Health Care

Requirements
Must have
• our logo

```html
<!DOCTYPE html>
<html lang="en">
<head>
<meta charset="utf-8">
<title>Certificate of Appreciation</title>
<link href="https://fonts.googleapis.com/css2?family=Poppins:ital,wght@0,500;0,600;1,500&family=Tinos&family=Pinyon+Script&display=swap" rel="stylesheet">
<style>
  :root {
    --navy: #15294a;
    --navy-light: #2c4a75;
    --navy-deep: #0f2040;
    --gold: #f2c21b;
    --gold-light: #fbe765;
    --gold-dark: #d3a21f;
    --paper: #ffffff;
    --ink: #15294a;
    --backdrop: #ececec;
  }
  html, body {
    margin: 0;
    width: 1200px;
    height: 1200px;
    overflow: hidden;
    background: var(--backdrop);
  }
  .certificate {
    position: absolute;
    left: 197px;
    top: 30px;
    width: 924px;
    height: 1308px;
    background: var(--paper);
    transform: scale(0.8716);
    transform-origin: 0 0;
    overflow: hidden;
    color: var(--ink);
  }
  .certificate__art { position: absolute; inset: 0; }
  .line { position: absolute; left: 0; width: 100%; text-align: center; margin: 0; }
  .emblem {
    position: absolute;
    left: 356px; top: 72px;
    width: 200px; height: 200px;
    border-radius: 50%;
    background: var(--navy);
    border: 4px solid var(--paper);
    box-shadow: 0 0 0 1px #c9ced8;
    display: flex; align-items: center; justify-content: center;
    text-align: center;
    font-family: "Poppins", sans-serif;
    font-weight: 600;
    font-size: 22px;
    line-height: 1.25;
    color: var(--paper);
  }
  .title {
    top: 292px;
    font-family: "Poppins", sans-serif;
    font-weight: 600;
    font-size: 70px;
    letter-spacing: 4px;
    line-height: 84px;
  }
  .subtitle {
    top: 371px;
    font-family: "Poppins", sans-serif;
    font-weight: 500;
    font-size: 24px;
    letter-spacing: 2.5px;
  }
  .recipient {
    top: 430px;
    font-family: "Pinyon Script", cursive;
    font-size: 84px;
    line-height: 120px;
  }
  .body-text, .signer, .registration, .notice, .address {
    font-family: "Tinos", serif;
  }
  .body-text { font-size: 23px; line-height: 33.5px; top: 555px; }
  .signature {
    position: absolute;
    top: 776px;
    width: 316px;
    text-align: center;
    font-family: "Tinos", serif;
  }
  .signature--left { left: 75px; }
  .signature--right { left: 536px; }
  .signature__rule { border-top: 2px dotted #7c889c; margin-bottom: 22px; }
  .signature__name { font-size: 20px; line-height: 24px; }
  .signature__role { font-size: 16px; line-height: 24px; }
  .registration { top: 905px; font-size: 22px; }
  .notice { top: 955px; font-size: 22.5px; line-height: 34.5px; }
  .address { top: 1081px; font-size: 22.5px; line-height: 34px; }
  .tagline {
    top: 1262px;
    font-family: "Poppins", sans-serif;
    font-style: italic;
    font-weight: 500;
    font-size: 21px;
    color: var(--paper);
  }
</style>
</head>
<body>
<main class="certificate">
  <svg class="certificate__art" viewBox="0 0 924 1308" width="924" height="1308" aria-hidden="true">
    <defs>
      <linearGradient id="navyTop" x1="0" y1="0" x2="1" y2="0">
        <stop offset="0" stop-color="#1a2f55"/>
        <stop offset="0.2" stop-color="#2e4b77"/>
        <stop offset="0.55" stop-color="#13274a"/>
        <stop offset="0.8" stop-color="#1b3d6b"/>
        <stop offset="1" stop-color="#13284b"/>
      </linearGradient>
      <linearGradient id="navyBottom" x1="0" y1="0" x2="1" y2="0">
        <stop offset="0" stop-color="#13284b"/>
        <stop offset="0.45" stop-color="#1e3f6e"/>
        <stop offset="1" stop-color="#152b50"/>
      </linearGradient>
      <linearGradient id="goldBand" x1="0" y1="0" x2="1" y2="0">
        <stop offset="0" stop-color="#d8a620"/>
        <stop offset="0.1" stop-color="#fbe765"/>
        <stop offset="0.35" stop-color="#f2c21b"/>
        <stop offset="0.65" stop-color="#d9a623"/>
        <stop offset="0.85" stop-color="#f5cf2a"/>
        <stop offset="1" stop-color="#fbe765"/>
      </linearGradient>
    </defs>
    <!-- top band -->
    <path d="M0,0 H924 V308 C800,300 650,260 500,190 C350,120 150,95 0,178 Z" fill="url(#goldBand)"/>
    <path d="M0,0 H924 V228 C800,240 650,215 500,150 C350,85 150,60 0,110 Z" fill="url(#navyTop)"/>
    <!-- bottom band -->
    <path d="M0,1078 C120,1190 300,1215 500,1195 C700,1172 820,1165 924,1173 V1308 H0 Z" fill="url(#goldBand)"/>
    <path d="M0,1148 C140,1240 330,1250 520,1232 C700,1215 840,1240 924,1262 V1308 H0 Z" fill="url(#navyBottom)"/>
    <!-- frame rules -->
    <line x1="42" y1="186" x2="42" y2="1083" stroke="#3b4a63" stroke-width="1.5"/>
    <line x1="883" y1="338" x2="883" y2="1163" stroke="#3b4a63" stroke-width="1.5"/>
  </svg>

  <div class="emblem">Meridia<br>Balance<br>Therapy</div>

  <h1 class="line title">CERTIFICATE</h1>
  <p class="line subtitle">OF APPRECIATION</p>

  <p class="line recipient">Tomas Arlenda</p>

  <p class="line body-text">has completed the fasciatherapy level I course<br>3 Days, 75-77 February 2020<br>Hafnarfjörður, Iceland 77 february 2020.</p>

  <div class="signature signature--left">
    <div class="signature__rule"></div>
    <div class="signature__name">Mr. JB Hollander</div>
    <div class="signature__role">Co-Director</div>
  </div>
  <div class="signature signature--right">
    <div class="signature__rule"></div>
    <div class="signature__name">Mr. RK Demiral</div>
    <div class="signature__role">Co-Director</div>
  </div>

  <p class="line registration">Registration number: 7 ICE 20</p>
  <p class="line notice">The Meridia Balance Therapy ongoing certification is contingent<br>upon meeting the requirements of the maintenance of the<br>certification of Fasciatherapy</p>
  <p class="line address">Meridiaweb BV, Tweede Lindengracht 14<br>1015KT Amsterdam, The Netherlands</p>

  <p class="line tagline">Specialists in fasciatherapy innovation</p>
</main>
</body>
</html>
```